Packaging Design Project - Organic Baby Skin Care

This project is to re-design our current organic baby skin care range labels. See here:

http://www.velvetmeadow.com.au/Baby-Care

The common complaint is that the pink is too girly for boys. For this reason I am not sure if I should keep the "Velvet Meadow Baby" Logo as it is a bit girly looking as well. So open to your ideas.

The size of the label will be approx 90 w x 70 h mm

Here is one range I like that is already similar to what I am already doing with the polka dots but in different pastels: http://www.tiptapstore.com/baby-skincare.html

Also another idea for a concept here with a beige/vintage look background: http://www.pinebarnstore.com/tiny_fern_naturals/tiny_fern_naturals_creamy_body_lotion-c482915p730218.html

Lastly, I also like these fun colourful, child like graphics of this range:

http://www.wrenhollownaturals.co.uk/brands/hush-drowsy-bear/

The range consists of:

Soothing Baby Salve in a white tube
Bubbly Fresh Baby Bath in a white 250ml bottle
Nana and Bibi Rubbing Oil in a white 100ml bottle
Quiet Night Relaxing Spray in a white 100ml bottle
Oat Cream Bar in a cardboard box

See packaging attached.

I will be presenting all the designs to a group of mother's for market research so they will be making the final decision - seeing they are the ones who will ultimately buy the product.

That is why I am open to a wide range of styles for this project.

Looking forward to seeing your work!

Any questions, let me know!
Updates

Hello Designers!

I have posted an update to include more information in the brief and also the AI logo file which shows the current packaging. Also images of the bottles of the current range. The bottles will be white boston round bottles not the tall boston as I am currently using.

many thanks

Loretta

Hello Designers

Just wanted to get an update on how you are going with your design submissions?

The deadline is this Saturday and we have received very few designs.

I await your reply.

thanks
Loretta

Reason: The deadline is drawing near and have not received enough designs. Please submit your designs as soon as you can. Many thanks Loretta Velvet Meadow

Target Market(s)

Mothers 25 - 40

Industry/Entity Type

Market Research

Requirements
Must have
• Organic/Natural feel, Stylish, Elegant, Gender Neutral to suit both sexes
Nice to have
• Vintage feel

```html
<!DOCTYPE html>
<html lang="en">
<head>
<meta charset="utf-8">
<title>Velvet Meadow Baby – Organic Oat Cream Bar</title>
<link rel="stylesheet" href="https://fonts.googleapis.com/css2?family=Sniglet&family=Arimo&display=swap">
<style>
  :root {
    --page: #f4f2f5;
    --lilac: #e6dce9;
    --lilac-light: #f1ebf3;
    --lilac-side: #cbbcd1;
    --lilac-side-light: #d9cddd;
    --pin: #d6bedb;
    --ink: #4a2218;
    --band: #f7f2dc;
    --badge: #e4dbe8;
  }
  * { margin: 0; padding: 0; box-sizing: border-box; }
  html, body { width: 841px; height: 1200px; overflow: hidden; }
  body {
    background: var(--page);
    position: relative;
    font-family: "Sniglet", "Comic Sans MS", sans-serif;
    color: var(--ink);
  }

  .side-panel {
    position: absolute; left: 0; top: 0; width: 190px; height: 1200px;
    background: linear-gradient(180deg, var(--lilac-side-light) 0%, var(--lilac-side) 45%, var(--lilac-side-light) 100%);
    display: flex; flex-direction: column; align-items: center; justify-content: center; gap: 80px;
  }
  .side-panel .badge { width: 96px; height: 96px; border-radius: 50%; background: var(--badge); }

  .front-panel {
    position: absolute; left: 190px; top: 0; width: 651px; height: 1200px;
    background: radial-gradient(ellipse at 50% 45%, var(--lilac-light) 0%, var(--lilac) 70%);
  }
  .dot-pattern { position: absolute; inset: 0; }

  .safety-pin {
    position: absolute; left: 40px; top: 100px; width: 380px; height: 56px;
    border-radius: 28px; background: var(--pin);
  }

  .label {
    position: absolute; left: 55px; top: 290px; width: 541px; height: 750px;
  }
  .label-frame { position: absolute; inset: 0; }
  .label-content {
    position: absolute; inset: 0;
    display: flex; flex-direction: column; align-items: center; justify-content: center;
    text-align: center; gap: 54px;
  }
  .brand { display: flex; align-items: center; gap: 14px; }
  .brand-mark { width: 30px; height: 30px; border-radius: 50%; background: var(--ink); }
  .brand-name { font-size: 34px; color: var(--ink); }
  .product-title { font-size: 66px; line-height: 1.2; font-weight: 400; }
  .net-size { font-size: 34px; font-family: "Arimo", Arial, sans-serif; }

  .info-band {
    position: absolute; left: 0; bottom: 0; width: 651px; height: 120px;
    background: var(--band);
    display: flex; flex-direction: column; align-items: center; justify-content: center;
    font-family: "Arimo", Arial, sans-serif; font-size: 27px; line-height: 1.3; color: #222;
  }
</style>
</head>
<body>
  <aside class="side-panel">
    <div class="badge"></div>
    <div class="badge"></div>
    <div class="badge"></div>
  </aside>

  <main class="front-panel">
    <div class="dot-pattern" role="img" aria-label="White polka dot pattern on lilac"></div>
    <div class="safety-pin" role="img" aria-label="Lilac safety pin illustration"></div>

    <section class="label">
      <svg class="label-frame" viewBox="0 0 541 750" aria-hidden="true">
        <path d="M44,6 H497 A38,38 0 0 0 535,44 V706 A38,38 0 0 0 497,744 H44 A38,38 0 0 0 6,706 V44 A38,38 0 0 0 44,6 Z"
              fill="none" stroke="#4a2218" stroke-width="6"/>
        <path d="M52,20 H489 A32,32 0 0 0 521,52 V698 A32,32 0 0 0 489,730 H52 A32,32 0 0 0 20,698 V52 A32,32 0 0 0 52,20 Z"
              fill="none" stroke="#4a2218" stroke-width="2"/>
      </svg>
      <div class="label-content">
        <div class="brand">
          <span class="brand-mark"></span>
          <p class="brand-name">Velvet Meadow Baby</p>
        </div>
        <h1 class="product-title">Organic<br>Oat Cream<br>Bar</h1>
        <p class="net-size">e 100g&nbsp; 3.5fl oz.</p>
      </div>
    </section>

    <footer class="info-band">
      <p>contains certified organic ingredients</p>
      <p>fragrance free</p>
    </footer>
  </main>
</body>
</html>
```